Business Card Design Project

Business Card design based on logo.

I need business card, letterhead, envelope, and if possible, Powerpoint slide template.

On front of business card: Just logo- and  my name and title:  Rosalind Pekar, Principal

On reverse-logo and the rest of the contact info:

4857 Orchard Lane
Davis, CA 95618
650-381-2276
rp@brindlestudyworks.example

On letterhead-Just logo at top, at bottom  the rest-very small along the bottom

On PPT slide-just the logo.

I also want to try a few other colors-I like lime/dark grey (not black) but would like to try Sienna, maybe also indigo or bright blue-green.

I forgot to add-

On the business card-switch to vertical on reverse side and put:

Reverse side-switch to vertical and list:

Rosalind Pekar
Principal
Brindle Study Works, LLC

650-381-2276

4857 Orchard Lane
Davis, CA 95618

Rosalind Pekar
Principal

650-381-2276

4857 Orchard Lane
Davis, CA 95618

I have another project at the same time-for Stationery. Feel free to submit to that one also.

That one includes letterhead, envelope, PPT slide, folder cover sheet-RP

Industry/Entity Type

Business

Requirements
Must have
• Must use logo-preferably lime green version-with gray, not black or just 2-tone -logo on colored background.

```html
<!DOCTYPE html>
<html lang="en">
<head>
<meta charset="utf-8">
<title>Brindle Study Works – Business Card</title>
<link rel="stylesheet" href="https://fonts.googleapis.com/css2?family=Source+Sans+3:wght@400;600;700&display=swap">
<style>
  :root {
    --backdrop: #2b2b2b;
    --card: #ffffff;
    --lime: #8cb62a;
    --graphite: #4a4a4c;
    --ink: #2e2e2e;
  }
  * { margin: 0; padding: 0; box-sizing: border-box; }
  html, body {
    width: 1200px; height: 722px; overflow: hidden;
    background: var(--backdrop);
    font-family: "Source Sans 3", "Helvetica Neue", Arial, sans-serif;
  }
  .canvas { position: relative; width: 1200px; height: 722px; }
  .card {
    position: absolute; width: 300px; height: 525px;
    background: var(--card); border-radius: 14px; overflow: hidden;
  }
  .card--front { left: 290px; top: 97px; }
  .card--back  { left: 611px; top: 99px; }

  .brand { position: absolute; left: 0; width: 100%; text-align: center; }
  .brand__dot {
    display: block; width: 34px; height: 34px; margin: 0 auto 30px;
    border-radius: 50%; background: var(--lime);
  }
  .brand__name {
    display: block; color: var(--graphite); font-weight: 600;
    font-size: 25px; letter-spacing: 3px; line-height: 1.15;
    text-transform: uppercase;
  }
  .card--front .brand { top: 185px; }
  .card--back .brand { top: 125px; }

  .website {
    position: absolute; top: 325px; width: 100%; text-align: center;
    font-size: 13px; letter-spacing: 1.3px; color: var(--ink); line-height: 1;
  }
  .website span { color: var(--lime); }

  .contact {
    position: absolute; top: 358px; width: 100%; text-align: center;
    color: var(--ink); font-size: 13px; line-height: 1.2;
  }
  .contact__name { font-size: 16px; font-weight: 700; color: var(--lime); }
  .contact__role { font-size: 13px; font-weight: 400; color: var(--ink); }
  .contact__line {
    margin-top: 9px; display: flex; justify-content: center;
    align-items: center; gap: 7px; line-height: 1;
  }
  .contact__line--first { margin-top: 16px; }
  .contact__line svg { width: 11px; height: 11px; fill: var(--lime); }
  .contact__company {
    margin-top: 22px; font-size: 15px; font-weight: 700; color: var(--lime); line-height: 1;
  }
  .contact__address { margin-top: 10px; line-height: 1; }
</style>
</head>
<body>
<main class="canvas">
  <section class="card card--front" aria-label="Card front">
    <div class="brand">
      <span class="brand__dot"></span>
      <span class="brand__name">Brindle<br>Study Works</span>
    </div>
    <p class="website">www.<span>brindlestudyworks</span>.example</p>
  </section>

  <section class="card card--back" aria-label="Card back">
    <div class="brand">
      <span class="brand__dot"></span>
      <span class="brand__name">Brindle<br>Study Works</span>
    </div>
    <div class="contact">
      <p><span class="contact__name">Rosalind Pekar,</span> <span class="contact__role">Principal</span></p>
      <p class="contact__line contact__line--first">
        <svg viewBox="0 0 24 24" aria-hidden="true"><path d="M6.6 10.8a15.1 15.1 0 0 0 6.6 6.6l2.2-2.2c.3-.3.7-.4 1-.2 1.1.4 2.3.6 3.6.6.6 0 1 .4 1 1V20c0 .6-.4 1-1 1A17 17 0 0 1 3 4c0-.6.4-1 1-1h3.5c.6 0 1 .4 1 1 0 1.3.2 2.5.6 3.6.1.3 0 .7-.2 1z"/></svg>
        650-381-2276
      </p>
      <p class="contact__line">
        <svg viewBox="0 0 24 24" aria-hidden="true"><path d="M2 5h20v14H2zm2 2v.5l8 5 8-5V7zm0 2.8V17h16V9.8l-8 5z"/></svg>
        rp@brindlestudyworks.example
      </p>
      <p class="contact__company">Brindle Study Works, LLC</p>
      <p class="contact__address">4857 Orchard Lane Davis, CA 95618</p>
    </div>
  </section>
</main>
</body>
</html>
```